Flyer-Design für bildenden Künstler
Die einzige Designerin, die es wirklich verstanden hat, mein ausführliches briefing in einem wunderschönen, eleganten und absolut einzigartigen Design umzusetzen. Die Zusammenarbeit war klasse, sie ist auf jede meiner Wünsche eingegangen und hat sie mit großer Geduld und Professionalität umgesetzt. Das hätte nicht besser laufen können. Bin begeistert, von ihrem künstlerischen Anspruch, dem feinen Sinn für Ästhetik und ihrer großen Kreativität.
Zielgruppe
Ich bin bildender Künstler, benötige einen außergewöhnlichen, sehr ästhetischen, einzigartigen, als Eyecatcher fungierenden, meine Kunst und Identität repräsentierenden Flyer zum Auslegen, um neue KundInnen zu gewinnen.
Aufgabenstellung
Er soll wenig Text beinhalten (ein Zitat, Anschrift und Kontaktmöglichkeiten, ein kleines statement zu meiner Kunstphilosophie), und Bilder meiner Kunst zeigen. Raum ist mir wichtig, genug Leerräume, damit ein in Szene gesetztes Zitat oder Foto meiner Kunstwerke gut wirken kann. Es soll Lust darauf machen, Anreiz bieten und Interesse wecken, auf meine homepage zu gehen. Die Einzigartigkeit meiner Kunst soll deutlich werden.
Die hochgelandenen Fotos zeigen meine Kunstwerke. Sie können als Hintergrundbild fungieren und dementsprechend auch die ganze Seite ausfüllen, sie können zugeschnitten werden und/oder mit Text überlagert sein. Manche Fotos (zum Beispiel die Kunstwerke mit Rahmen) eignen sich dagegen, sie auf einer ganzen Seite zu zeigen, ohne einen Text dazu. So eine Seite würde ich jedenfalls gerne dabei haben, wo ein Kunstwerk für sich alleine auf einer ganzen Seite dargestellt wird. 1O4A2598 oder 1O4A6076a bieten sich dafür an (diese und alle anderen Fotos sind zum Teil komprimiert und zugeschnitten; falls gewünscht bzw. die Qualität nicht gut ist, kann ich das Originalfoto senden, das unkomprimiert und nicht zugeschnitten ist. Auch kann die Helligkeit oder die Farbqualität verbessert werden, falls notwendig). Nicht alle Kunstbilder müssen verwendet werden.
Ich bin offen für jedes Flyerformat, tendiere zu einem ein 2 oder 3-seitigen Falzflyer hochkant oder im Querformat. Bin aber offen für Ideen und Vorschläge.
Die Texte unter der Datei 'Texte, Adresse, Zitate' enthalten einen kleinen Text, der verwendet werden soll. Unter 'Text für die Titelseite' ist ein Vorschlag für die Titelseite zu finden. Die Adresse muss vollständig erscheinen, und unter 'Zitate' sind mehrere meiner Zitate - auch davon soll eines verwendet werden.
BITTE AUSSCHLIEßLICH DIE FOTOS UND TEXTE VERWENDEN, DIE ICH HOCHGELADEN HABE, UND NICHTS VON MEINEN HOMEPAGES NEHMEN. DANKE!

```html
<!DOCTYPE html>
<html lang="de">
<head>
<meta charset="utf-8">
<title>Flyer – Zitat</title>
<link rel="stylesheet" href="https://fonts.googleapis.com/css2?family=Poiret+One&display=swap">
<style>
  :root {
    --paper: #ffffff;
    --ink: #1f1f1f;
    --artwork-highlight: #5fd3f2;
    --artwork-light: #3cc2e8;
    --artwork-mid: #22a6d2;
    --artwork-deep: #11719a;
    --artwork-shadow: #0a4a66;
  }
  html, body {
    margin: 0;
    padding: 0;
    width: 1200px;
    height: 1200px;
    overflow: hidden;
    background: var(--paper);
  }
  .flyer-page {
    position: relative;
    width: 1200px;
    height: 1200px;
    background: var(--paper);
    display: flex;
  }
  .artwork-panel {
    width: 708px;
    height: 1200px;
    flex: none;
    background:
      radial-gradient(ellipse 170px 150px at 25% 12%, var(--artwork-highlight) 0%, transparent 70%),
      radial-gradient(ellipse 200px 170px at 62% 48%, var(--artwork-highlight) 0%, transparent 70%),
      radial-gradient(ellipse 160px 150px at 18% 72%, var(--artwork-highlight) 0%, transparent 70%),
      radial-gradient(ellipse 190px 170px at 72% 80%, var(--artwork-light) 0%, transparent 70%),
      radial-gradient(ellipse 150px 140px at 88% 30%, var(--artwork-light) 0%, transparent 70%),
      radial-gradient(ellipse 120px 90px at 70% 20%, var(--artwork-shadow) 0%, transparent 70%),
      radial-gradient(ellipse 90px 120px at 8% 38%, var(--artwork-deep) 0%, transparent 70%),
      radial-gradient(ellipse 110px 80px at 38% 62%, var(--artwork-deep) 0%, transparent 70%),
      radial-gradient(ellipse 100px 90px at 45% 92%, var(--artwork-deep) 0%, transparent 70%),
      linear-gradient(160deg, var(--artwork-light) 0%, var(--artwork-mid) 55%, var(--artwork-deep) 100%);
  }
  .quote-column {
    flex: 1;
    padding: 250px 0 0 63px;
  }
  .quote {
    margin: 0;
    font-family: "Poiret One", sans-serif;
    font-size: 32px;
    line-height: 44px;
    letter-spacing: 0.2px;
    color: var(--ink);
    white-space: nowrap;
  }
</style>
</head>
<body>
  <main class="flyer-page">
    <div class="artwork-panel" role="img" aria-label="Fotografie eines Kunstwerks: dicht gedrängte, schwammartige, türkisblaue Strukturen"></div>
    <section class="quote-column">
      <p class="quote">Die Suche nach der<br>Wahrheit führt nur über<br>die Distanz zur Realität.</p>
    </section>
  </main>
</body>
</html>
```